VornaDesk website (https://vornadesk.example) re-design

Website purposed for providing general information on products we develop and offer. Products are software specific to online poker players.
Software not playful but complex technological solutions so website should look neatly and professional.
More details on the project you may find in this document:
https://papers.quillnest.example/doc/7TmR2kZpW9xLqB4nVc8YdHs3EfGaJu6KoPi1NwXe/edit#section=s.qkmz4f81b2rn
Or below:
Technology: preferable bootstrap, but not critical
CrossPlatform: Desktop/Mobile
Pages:
Main (Current https://vornadesk.example/)
Video, Room list, Features, Price, Contacts
Partner section (whom we work with)
Documentation and FAQ links
Login (Current https://vornadesk.example/Login/Login)
SignUp/Password recovery (https://vornadesk.example/Signup/Signup, https://vornadesk.example/Login/RemindPassword)
License token (unique and assigned per customer). Need an option to copy to clipboard from Dashboard screen.
Download link for latest product version.
Subs end date to display
Manuals FAQ links
Buy and renew subscription
Notes: Group everything related to subscription into one logic block on the screen.
FAQ (https://vornadesk.example/Home/FAQ).
Simple and comfortable in usage faq.
Notes: Combine all the steps into one screen.
Make download trial which leads to registration!
Target Market(s)
Online poker players
Number of Pages Required
5+ page

```html
<!DOCTYPE html>
<html lang="en">
<head>
<meta charset="utf-8">
<title>VornaDesk — Poker Software</title>
<link href="https://fonts.googleapis.com/css2?family=Ubuntu:wght@400;500;700&family=Roboto+Condensed:wght@400&display=swap" rel="stylesheet">
<style>
:root{
  --ink:#111;
  --muted:#555;
  --blue:#0b86c9;
  --blue-light:#3aa3dc;
  --plan-free:#8aafd8;
  --plan-std:#2e74b5;
  --plan-gold:#0f91d8;
  --green:#c5dc7b;
  --star:#a8cf68;
  --dark:#0d0d0d;
  --panel:#1b1b1b;
  --panel-2:#222;
  --grey-bg:#f1f1f1;
  --line:#d9d9d9;
}
*{box-sizing:border-box;margin:0;padding:0}
html,body{width:1200px;height:3835px;overflow:hidden}
body{font-family:"Ubuntu",sans-serif;color:var(--ink);background:#fff;position:relative}
a{color:inherit;text-decoration:none}
.abs{position:absolute}

/* header */
.site-header{position:absolute;top:0;left:0;width:1200px;height:63px;background:#fff}
.brand{position:absolute;left:157px;top:18px;font-size:23px;font-weight:700}
.main-nav{position:absolute;right:157px;top:21px;display:flex;gap:36px;font-size:15px;font-weight:500}

/* hero */
.hero{position:absolute;top:63px;left:0;width:1200px;height:480px;
  background:radial-gradient(ellipse at 50% 50%,#2f5a3e 0%,#1f3f2b 60%,#13261a 100%)}
.play-btn{position:absolute;left:544px;top:186px}

/* section titles */
.section-title{position:absolute;left:0;width:1200px;text-align:center;font-size:42px;font-weight:500;letter-spacing:.3px}

/* rooms */
.room{position:absolute;width:285px}
.room-image{width:285px;height:189px;background:linear-gradient(160deg,#2a2a2a,#050505);border:1px solid #ccc}
.room-name{margin-top:22px;font-size:22px;font-weight:500}
.rating{display:flex;align-items:center;gap:3px;margin-top:6px;font-size:9px;color:var(--muted)}
.rating i{width:10px;height:10px;background:var(--star);transform:rotate(45deg) scale(.75);display:inline-block}
.rating b{font-weight:400;margin:0 8px 0 6px;color:#333}
.offer{margin-top:11px;font-family:"Roboto Condensed",sans-serif;font-size:16px;color:var(--blue)}
.room-text{margin-top:2px;font-size:11.5px;line-height:16px;color:var(--muted)}
.platforms{display:flex;gap:6px;margin-top:18px}
.platforms span{width:35px;height:35px;border-radius:50%;background:var(--blue);display:flex;align-items:center;justify-content:center}
.see-all{position:absolute;left:525px;top:1533px;width:150px;height:47px;background:var(--green);font-size:16px;font-weight:700;display:flex;align-items:center;justify-content:center;gap:6px}

/* features */
.features{position:absolute;top:1675px;left:0;width:1200px;height:687px;
  background:linear-gradient(180deg,#0b0b0b 0%,#0b0b0b 80%,#1f4a33 100%)}
.features-art{position:absolute;left:0;top:250px;width:420px;height:437px;
  background:radial-gradient(ellipse at 50% 55%,#d9d9d9 0%,#8c2a2a 45%,#1c3a2a 80%,transparent 100%)}
.features-title{position:absolute;left:562px;top:70px;font-size:42px;font-weight:500;color:#fff}
.feature-panel{position:absolute;left:564px;top:137px;width:479px;height:474px;background:var(--panel)}
.tabs{display:flex;height:52px}
.tab{width:50%;display:flex;align-items:center;padding-left:66px;color:#fff;font-size:16px;font-weight:500}
.tab.client{background:var(--blue)}
.tab.table{background:var(--blue-light);padding-left:42px}
.feature-cols{display:flex;height:422px}
.feature-cols ul{list-style:none;width:50%;padding:16px 0 0 66px;font-size:11.5px;color:#bbb;line-height:24.7px}
.feature-cols ul.right{background:var(--panel-2);padding-left:42px}

/* pricing */
.plan{position:absolute;top:2527px;width:285px;height:565px;border:1px solid var(--line);background:#fff}
.plan-head{height:138px;text-align:center;color:#fff;padding-top:32px}
.plan-head small{display:block;font-size:10px;letter-spacing:.3px}
.plan-head h3{font-size:27px;font-weight:500;letter-spacing:1px;margin-top:8px}
.price-box{position:absolute;left:35px;top:96px;width:214px;height:132px;background:#fff;box-shadow:0 2px 8px rgba(0,0,0,.18);text-align:center;padding-top:24px}
.price-box strong{font-size:38px;font-weight:700}
.price-box p{font-size:9px;color:#777;line-height:13px;margin:10px 22px 0}
.plan-list{list-style:none;position:absolute;left:26px;top:260px;width:240px}
.plan-list li{display:flex;gap:12px;font-size:11.5px;line-height:17px;color:#555;margin-bottom:25px}
.plan-list svg{flex:none;margin-top:3px}
.buy{position:absolute;left:67px;top:515px;width:150px;height:48px;color:#fff;font-size:16px;font-weight:700;display:flex;align-items:center;justify-content:center}
.free .plan-head,.free .buy{background:var(--plan-free)} .free strong{color:var(--plan-free)}
.std .plan-head,.std .buy{background:var(--plan-std)} .std strong{color:var(--plan-std)}
.gold .plan-head,.gold .buy{background:var(--plan-gold)} .gold strong{color:var(--plan-gold)}

/* partners */
.partners{position:absolute;top:3185px;left:0;width:1200px;height:363px;background:var(--grey-bg)}
.partner{position:absolute;top:148px;height:145px;background:#fff;display:flex;align-items:center;justify-content:center}

/* contact */
.contact{position:absolute;top:3548px;left:0;width:1200px;height:287px;background:var(--dark);color:#fff}
.contact-art{position:absolute;right:0;top:0;width:400px;height:287px;
  background:radial-gradient(ellipse at 70% 45%,#e9e9e9 0%,#7a5a4a 30%,#2a1a1a 55%,transparent 75%)}
.contact h2{position:absolute;left:157px;top:57px;font-size:40px;font-weight:500}
.doc-links{position:absolute;left:157px;top:131px;display:flex;gap:32px;font-size:16px;color:var(--blue-light)}
.doc-links a{text-decoration:underline}
.contact p{position:absolute;left:157px;font-size:16px}
.contact p a{color:var(--blue-light);text-decoration:underline}
</style>
</head>
<body>

<header class="site-header">
  <a class="brand" href="https://vornadesk.example/">VornaDesk</a>
  <nav class="main-nav">
    <a href="https://vornadesk.example/">Home</a>
    <a href="https://vornadesk.example/Login/Login">Login</a>
    <a href="https://vornadesk.example/Signup/Signup">SignUp</a>
    <a href="#">Dashboard</a>
    <a href="https://vornadesk.example/Home/FAQ">FAQ</a>
  </nav>
</header>

<section class="hero" role="img" aria-label="Video still: hands dealing cards and chips on a green poker table">
  <svg class="play-btn" width="112" height="112" viewBox="0 0 112 112" aria-hidden="true">
    <circle cx="56" cy="56" r="51" fill="none" stroke="#fff" stroke-width="7"/>
    <path d="M44 34 L78 56 L44 78 Z" fill="#fff"/>
  </svg>
</section>

<h2 class="section-title" style="top:627px">BEST POCKER ROOMS</h2>

<!-- room cards -->
<div class="room" style="left:157px;top:698px">
  <div class="room-image" role="img" aria-label="Room artwork: red dragon on dark background"></div>
  <div class="room-name">CrimsonCrest Cards</div>
  <div class="rating"><i></i><i></i><i></i><i></i><i></i><b>9.4</b>Editor's rating</div>
  <div class="offer">Free $83+100% up to $ 333 / T&amp;C's apply</div>
  <p class="room-text">Lorem ipsum dolor sit amet, consectetur adipiscing elit. Aenean scelerisque, tellus at.</p>
  <div class="platforms"><span><svg width="16" height="16" viewBox="0 0 16 16"><rect x="1" y="2" width="14" height="9" rx="1" fill="#fff"/><rect x="5" y="12" width="6" height="2" fill="#fff"/></svg></span><span><svg width="16" height="16" viewBox="0 0 16 16"><rect x="4" y="1" width="8" height="14" rx="1.5" fill="#fff"/></svg></span><span><svg width="16" height="16" viewBox="0 0 16 16"><rect x="2" y="2" width="12" height="12" rx="1.5" fill="#fff"/></svg></span></div>
</div>
<div class="room" style="left:457px;top:698px">
  <div class="room-image" role="img" aria-label="Room artwork: gold spade emblem on dark background"></div>
  <div class="room-name">TrueDeal Tables</div>
  <div class="rating"><i></i><i></i><i></i><i></i><i></i><b>9.4</b>Editor's rating</div>
  <div class="offer">Free $83+100% up to $ 333 / T&amp;C's apply</div>
  <p class="room-text">Lorem ipsum dolor sit amet, consectetur adipiscing elit. Aenean scelerisque, tellus at.</p>
  <div class="platforms"><span><svg width="16" height="16" viewBox="0 0 16 16"><rect x="1" y="2" width="14" height="9" rx="1" fill="#fff"/><rect x="5" y="12" width="6" height="2" fill="#fff"/></svg></span><span><svg width="16" height="16" viewBox="0 0 16 16"><rect x="4" y="1" width="8" height="14" rx="1.5" fill="#fff"/></svg></span><span><svg width="16" height="16" viewBox="0 0 16 16"><rect x="2" y="2" width="12" height="12" rx="1.5" fill="#fff"/></svg></span></div>
</div>
<div class="room" style="left:757px;top:698px">
  <div class="room-image" role="img" aria-label="Room artwork: gold spade badge on black background"></div>
  <div class="room-name">OpenFold</div>
  <div class="rating"><i></i><i></i><i></i><i></i><i></i><b>9.4</b>Editor's rating</div>
  <div class="offer">Free $83+100% up to $ 333 / T&amp;C's apply</div>
  <p class="room-text">Lorem ipsum dolor sit amet, consectetur adipiscing elit. Aenean scelerisque, tellus at.</p>
  <div class="platforms"><span><svg width="16" height="16" viewBox="0 0 16 16"><rect x="1" y="2" width="14" height="9" rx="1" fill="#fff"/><rect x="5" y="12" width="6" height="2" fill="#fff"/></svg></span><span><svg width="16" height="16" viewBox="0 0 16 16"><rect x="4" y="1" width="8" height="14" rx="1.5" fill="#fff"/></svg></span><span><svg width="16" height="16" viewBox="0 0 16 16"><rect x="2" y="2" width="12" height="12" rx="1.5" fill="#fff"/></svg></span></div>
</div>

<div class="room" style="left:157px;top:1112px">
  <div class="room-image" role="img" aria-label="Room artwork: gold lettering on black background"></div>
  <div class="room-name">DeckMonarch East</div>
  <div class="rating"><i></i><i></i><i></i><i></i><i></i><b>9.4</b>Editor's rating</div>
  <div class="offer">Free $83+100% up to $ 333 / T&amp;C's apply</div>
  <p class="room-text">Lorem ipsum dolor sit amet, consectetur adipiscing elit. Aenean scelerisque, tellus at.</p>
  <div class="platforms"><span><svg width="16" height="16" viewBox="0 0 16 16"><rect x="1" y="2" width="14" height="9" rx="1" fill="#fff"/><rect x="5" y="12" width="6" height="2" fill="#fff"/></svg></span><span><svg width="16" height="16" viewBox="0 0 16 16"><rect x="4" y="1" width="8" height="14" rx="1.5" fill="#fff"/></svg></span><span><svg width="16" height="16" viewBox="0 0 16 16"><rect x="2" y="2" width="12" height="12" rx="1.5" fill="#fff"/></svg></span></div>
</div>
<div class="room" style="left:457px;top:1112px">
  <div class="room-image" role="img" aria-label="Room artwork: teal diamond emblem on black background"></div>
  <div class="room-name">RiverLine Poker</div>
  <div class="rating"><i></i><i></i><i></i><i></i><i></i><b>9.4</b>Editor's rating</div>
  <div class="offer">Free $83+100% up to $ 333 / T&amp;C's apply</div>
  <p class="room-text">Lorem ipsum dolor sit amet, consectetur adipiscing elit. Aenean scelerisque, tellus at.</p>
  <div class="platforms"><span><svg width="16" height="16" viewBox="0 0 16 16"><rect x="1" y="2" width="14" height="9" rx="1" fill="#fff"/><rect x="5" y="12" width="6" height="2" fill="#fff"/></svg></span><span><svg width="16" height="16" viewBox="0 0 16 16"><rect x="4" y="1" width="8" height="14" rx="1.5" fill="#fff"/></svg></span><span><svg width="16" height="16" viewBox="0 0 16 16"><rect x="2" y="2" width="12" height="12" rx="1.5" fill="#fff"/></svg></span></div>
</div>
<div class="room" style="left:757px;top:1112px">
  <div class="room-image" role="img" aria-label="Room artwork: metallic lettering over a spade on black background"></div>
  <div class="room-name">Luckwell (ex Tealeaf)</div>
  <div class="rating"><i></i><i></i><i></i><i></i><i></i><b>9.4</b>Editor's rating</div>
  <div class="offer">Free $83+100% up to $ 333 / T&amp;C's apply</div>
  <p class="room-text">Lorem ipsum dolor sit amet, consectetur adipiscing elit. Aenean scelerisque, tellus at.</p>
  <div class="platforms"><span><svg width="16" height="16" viewBox="0 0 16 16"><rect x="1" y="2" width="14" height="9" rx="1" fill="#fff"/><rect x="5" y="12" width="6" height="2" fill="#fff"/></svg></span><span><svg width="16" height="16" viewBox="0 0 16 16"><rect x="4" y="1" width="8" height="14" rx="1.5" fill="#fff"/></svg></span><span><svg width="16" height="16" viewBox="0 0 16 16"><rect x="2" y="2" width="12" height="12" rx="1.5" fill="#fff"/></svg></span></div>
</div>

<a class="see-all" href="#">See All <svg width="12" height="12" viewBox="0 0 12 12"><path d="M1 6h9M6 2l4 4-4 4" stroke="#111" stroke-width="1.6" fill="none"/></svg></a>

<!-- features -->
<section class="features">
  <div class="features-art" role="img" aria-label="Photo: two aces on stacks of casino chips"></div>
  <h2 class="features-title">OUR FEATUREDS</h2>
  <div class="feature-panel">
    <div class="tabs"><div class="tab client">Client Features</div><div class="tab table">Table Features</div></div>
    <div class="feature-cols">
      <ul>
        <li>Preview</li><li>Lobby View</li><li>Mini Table View</li><li>Summit Reward Points</li>
        <li>Real-time Game History</li><li>Multicurrency Options</li><li>Real-time Transaction</li>
        <li>HistoryFunctionality</li><li>Live Support</li><li>Auto Re-buy in</li><li>Tournaments</li>
        <li>Toast Notifications</li><li>Widget Bar</li><li>Buy-in &amp; Fee</li><li>Consolidation</li>
      </ul>
      <ul class="right">
        <li>Settings</li><li>Four Color Deck Option</li><li>Keyboard Play Support</li><li>Player Notes</li>
        <li>Buddy List</li><li>Hand History Replay Tool</li><li>Quick Deposit</li><li>Functionality</li>
        <li>Configurable Betting</li><li>Buttons</li><li>Time Bank</li><li>Spinner Tables</li>
        <li>Cash Table Groups</li><li>Tournament Pop-up &amp;</li><li>Notification Settings</li>
      </ul>
    </div>
  </div>
</section>

<!-- pricing -->
<h2 class="section-title" style="top:2445px">OUR PRICE PLANS</h2>

<div class="plan free" style="left:157px">
  <div class="plan-head"><small>PRICE TABLE</small><h3>FREE PLAN</h3></div>
  <div class="price-box"><strong>$0.00</strong><p>Nam consectetur euismod porta. Duis posuere est ac viverra volutpat.</p></div>
  <ul class="plan-list">
    <li><svg width="20" height="20" viewBox="0 0 20 20"><circle cx="10" cy="10" r="8.5" fill="none" stroke="#a8cf68" stroke-width="1.3"/><path d="M6 10.2l2.7 2.7L14 7.5" fill="none" stroke="#a8cf68" stroke-width="1.4"/></svg><span>Nam consectetur euismod porta.<br>Duis posuere est ac viverra volutpat.</span></li>
    <li><svg width="20" height="20" viewBox="0 0 20 20"><circle cx="10" cy="10" r="8.5" fill="none" stroke="#a8cf68" stroke-width="1.3"/><path d="M6 10.2l2.7 2.7L14 7.5" fill="none" stroke="#a8cf68" stroke-width="1.4"/></svg><span>Nam consectetur euismod porta.<br>Duis posuere est ac viverra volutpat.</span></li>
    <li><svg width="20" height="20" viewBox="0 0 20 20"><circle cx="10" cy="10" r="8.5" fill="none" stroke="#a8cf68" stroke-width="1.3"/><path d="M6 10.2l2.7 2.7L14 7.5" fill="none" stroke="#a8cf68" stroke-width="1.4"/></svg><span>Nam consectetur euismod porta.<br>Duis posuere est ac viverra volutpat.</span></li>
    <li><svg width="20" height="20" viewBox="0 0 20 20"><circle cx="10" cy="10" r="8.5" fill="none" stroke="#a8cf68" stroke-width="1.3"/><path d="M6 10.2l2.7 2.7L14 7.5" fill="none" stroke="#a8cf68" stroke-width="1.4"/></svg><span>Nam consectetur euismod porta.<br>Duis posuere est ac viverra volutpat.</span></li>
  </ul>
  <a class="buy" href="#">Buy Now</a>
</div>

<div class="plan std" style="left:458px">
  <div class="plan-head"><small>PRICE TABLE</small><h3>STANDARD PLAN</h3></div>
  <div class="price-box"><strong>$55.00</strong><p>Nam consectetur euismod porta. Duis posuere est ac viverra volutpat.</p></div>
  <ul class="plan-list">
    <li><svg width="20" height="20" viewBox="0 0 20 20"><circle cx="10" cy="10" r="8.5" fill="none" stroke="#a8cf68" stroke-width="1.3"/><path d="M6 10.2l2.7 2.7L14 7.5" fill="none" stroke="#a8cf68" stroke-width="1.4"/></svg><span>Nam consectetur euismod porta.<br>Duis posuere est ac viverra volutpat.</span></li>
    <li><svg width="20" height="20" viewBox="0 0 20 20"><circle cx="10" cy="10" r="8.5" fill="none" stroke="#a8cf68" stroke-width="1.3"/><path d="M6 10.2l2.7 2.7L14 7.5" fill="none" stroke="#a8cf68" stroke-width="1.4"/></svg><span>Nam consectetur euismod porta.<br>Duis posuere est ac viverra volutpat.</span></li>
    <li><svg width="20" height="20" viewBox="0 0 20 20"><circle cx="10" cy="10" r="8.5" fill="none" stroke="#a8cf68" stroke-width="1.3"/><path d="M6 10.2l2.7 2.7L14 7.5" fill="none" stroke="#a8cf68" stroke-width="1.4"/></svg><span>Nam consectetur euismod porta.<br>Duis posuere est ac viverra volutpat.</span></li>
    <li><svg width="20" height="20" viewBox="0 0 20 20"><circle cx="10" cy="10" r="8.5" fill="none" stroke="#a8cf68" stroke-width="1.3"/><path d="M6 10.2l2.7 2.7L14 7.5" fill="none" stroke="#a8cf68" stroke-width="1.4"/></svg><span>Nam consectetur euismod porta.<br>Duis posuere est ac viverra volutpat.</span></li>
  </ul>
  <a class="buy" href="#">Buy Now</a>
</div>

<div class="plan gold" style="left:759px">
  <div class="plan-head"><small>PRICE TABLE</small><h3>GOLDEN PLAN</h3></div>
  <div class="price-box"><strong>$95.00</strong><p>Nam consectetur euismod porta. Duis posuere est ac viverra volutpat.</p></div>
  <ul class="plan-list">
    <li><svg width="20" height="20" viewBox="0 0 20 20"><circle cx="10" cy="10" r="8.5" fill="none" stroke="#a8cf68" stroke-width="1.3"/><path d="M6 10.2l2.7 2.7L14 7.5" fill="none" stroke="#a8cf68" stroke-width="1.4"/></svg><span>Nam consectetur euismod porta.<br>Duis posuere est ac viverra volutpat.</span></li>
    <li><svg width="20" height="20" viewBox="0 0 20 20"><circle cx="10" cy="10" r="8.5" fill="none" stroke="#a8cf68" stroke-width="1.3"/><path d="M6 10.2l2.7 2.7L14 7.5" fill="none" stroke="#a8cf68" stroke-width="1.4"/></svg><span>Nam consectetur euismod porta.<br>Duis posuere est ac viverra volutpat.</span></li>
    <li><svg width="20" height="20" viewBox="0 0 20 20"><circle cx="10" cy="10" r="8.5" fill="none" stroke="#a8cf68" stroke-width="1.3"/><path d="M6 10.2l2.7 2.7L14 7.5" fill="none" stroke="#a8cf68" stroke-width="1.4"/></svg><span>Nam consectetur euismod porta.<br>Duis posuere est ac viverra volutpat.</span></li>
    <li><svg width="20" height="20" viewBox="0 0 20 20"><circle cx="10" cy="10" r="8.5" fill="none" stroke="#a8cf68" stroke-width="1.3"/><path d="M6 10.2l2.7 2.7L14 7.5" fill="none" stroke="#a8cf68" stroke-width="1.4"/></svg><span>Nam consectetur euismod porta.<br>Duis posuere est ac viverra volutpat.</span></li>
  </ul>
  <a class="buy" href="#">Buy Now</a>
</div>

<!-- partners -->
<section class="partners">
  <h2 class="section-title" style="top:42px">OUR PARTNERS</h2>
  <div class="partner" style="left:143px;width:150px"><svg width="56" height="56" aria-label="Partner badge"><rect x="4" y="4" width="48" height="48" rx="6" fill="#e8a33a"/></svg></div>
  <div class="partner" style="left:298px;width:200px"><svg width="56" height="56" aria-label="Partner badge"><circle cx="28" cy="28" r="24" fill="#2ab3a0"/></svg></div>
  <div class="partner" style="left:502px;width:185px"><svg width="56" height="56" aria-label="Partner badge"><rect x="4" y="4" width="48" height="48" rx="6" fill="#1f8fa4"/></svg></div>
  <div class="partner" style="left:691px;width:185px"><svg width="56" height="56" aria-label="Partner badge"><circle cx="28" cy="28" r="24" fill="#3aa86b"/></svg></div>
  <div class="partner" style="left:880px;width:177px"><svg width="56" height="56" aria-label="Partner badge"><rect x="4" y="4" width="48" height="48" rx="6" fill="#b2247a"/></svg></div>
</section>

<!-- contact -->
<footer class="contact">
  <div class="contact-art" role="img" aria-label="Photo: hand holding two aces above scattered chips"></div>
  <h2>CONTACT US</h2>
  <div class="doc-links">
    <a href="https://papers.quillnest.example/doc/7TmR2kZpW9xLqB4nVc8YdHs3EfGaJu6KoPi1NwXe/edit#section=s.qkmz4f81b2rn">Documentation</a>
    <a href="https://vornadesk.example/Home/FAQ">Installation manual FAQ</a>
  </div>
  <p style="top:160px">For any questions contact us via <a href="mailto:help@vornadesk.example">help@vornadesk.example</a></p>
  <p style="top:192px">© 2019 VornaDesk | All Rights Reserved | Terms and Agreement</p>
</footer>

</body>
</html>
```